Brenmore Timber Co website design

I have created an attached txt document with specifics of what I am looking for. The short version is that I am looking for a website design for a lumber yard/building materials store. They currently do not have a website other than a simple place holder. I have included several example websites of his direct competitors as well as made a note as to which one is the best example and the design he really likes. The txt document goes in depth as to navigation, points of interest and contact information. Unfortunately like most clients the logo files sucks. I am not sure why people don't have a good logo file.

```html
<!DOCTYPE html>
<html lang="en">
<head>
<meta charset="utf-8">
<title>Brenmore Timber Co</title>
<link rel="stylesheet" href="https://fonts.googleapis.com/css2?family=Jost:wght@400;500;600;700&display=swap">
<style>
:root{
  --green:#2f7a32;
  --green-dark:#256428;
  --brown:#4a1608;
  --brown-btn:#4b1b0c;
  --ink:#222;
  --muted:#3a3a3a;
  --white:#fff;
}
*{margin:0;padding:0;box-sizing:border-box}
html,body{width:1200px;height:3670px;overflow:hidden;background:var(--white)}
body{font-family:"Jost",sans-serif;color:var(--ink);position:relative}
.abs{position:absolute}
.topbar{left:0;top:0;width:1200px;height:58px;background:var(--green);color:var(--white);font-size:15px}
.topbar .phone{left:144px;top:18px;display:flex;align-items:center;gap:6px}
.topbar .addr{right:144px;top:18px;display:flex;align-items:center;gap:8px}
.brand{left:142px;top:80px;width:200px;text-align:center;color:var(--green-dark);font-weight:700;font-size:21px;line-height:24px}
.brand .mark{width:40px;height:40px;background:var(--green-dark);margin:0 auto 8px}
.nav{right:142px;top:141px;display:flex;gap:0;font-size:15px;font-weight:500}
.nav a{color:var(--ink);text-decoration:none;padding:4px 10px}
.nav a.active{background:var(--green);color:var(--white)}
.hero{left:0;top:218px;width:1200px;height:559px;background:linear-gradient(180deg,#8d9296 0%,#a5a9ab 22%,#7a6e5c 40%,#8b7b63 55%,#c9bca6 72%,#ddd3c2 100%)}
.hero-title{left:0;top:432px;width:1200px;text-align:center;color:var(--white);font-weight:700;font-size:51px;line-height:58px;letter-spacing:1px}
.btn{display:flex;align-items:center;justify-content:center;color:var(--white);background:var(--green);font-weight:600;text-decoration:none}
.explore{left:479px;top:626px;width:242px;height:60px;font-size:34px;letter-spacing:1px}
.dots{left:552px;top:712px;display:flex;gap:5px}
.dots span{width:14px;height:14px;border:1.5px solid #111;border-radius:50%;background:var(--white)}
.dots span.on{background:#111;box-shadow:inset 0 0 0 2px var(--white)}
.arrow{width:22px;height:30px}
.section-title{left:0;width:1200px;text-align:center;color:var(--brown);font-weight:700;font-size:31px;letter-spacing:1.5px}
.card-title{width:218px;text-align:center;font-size:26px;font-weight:500;color:var(--ink);letter-spacing:.5px}
.photo{width:218px;height:245px}
.card-text{width:218px;text-align:center;font-size:12.5px;line-height:20px;color:var(--muted)}
.small-btn{width:171px;height:41px;font-size:19px;letter-spacing:.5px}
.quote-btn{background:var(--brown-btn)}
.lead{left:144px;width:912px;text-align:center;font-size:12.5px;line-height:20px;color:var(--muted)}
.quote-band{left:0;top:2676px;width:1200px;height:414px;background:linear-gradient(180deg,#2c2a27 0%,#3b3630 50%,#2a2723 100%)}
.quote-band .lead{color:#e8e8e8}
.footer-head{font-size:24px;font-weight:500;letter-spacing:.5px}
.links{font-size:14.5px;line-height:23.5px;color:var(--muted);letter-spacing:.3px}
.about{left:561px;top:3242px;width:495px;font-size:14.5px;line-height:20px;color:var(--muted)}
.rule{left:561px;top:3371px;width:263px;height:1px;background:#999}
.social{width:40px;height:40px;border-radius:50%}
.bottombar{left:0;top:3541px;width:1200px;height:129px;background:var(--green);color:var(--white);font-size:11.5px;font-weight:600;line-height:24px}
</style>
</head>
<body>

<div class="abs topbar">
  <div class="abs phone">
    <svg width="16" height="16" viewBox="0 0 24 24" fill="#fff"><path d="M6.6 10.8a15.1 15.1 0 0 0 6.6 6.6l2.2-2.2a1 1 0 0 1 1-.25 11.4 11.4 0 0 0 3.6.57 1 1 0 0 1 1 1V20a1 1 0 0 1-1 1A17 17 0 0 1 3 4a1 1 0 0 1 1-1h3.5a1 1 0 0 1 1 1c0 1.25.2 2.45.57 3.57a1 1 0 0 1-.25 1z"/></svg>
    <span>(555) 410-2286</span>
  </div>
  <div class="abs addr">
    <svg width="12" height="16" viewBox="0 0 12 16" fill="#fff"><path d="M6 0a6 6 0 0 0-6 6c0 4.5 6 10 6 10s6-5.5 6-10a6 6 0 0 0-6-6zm0 8.2A2.2 2.2 0 1 1 6 3.8a2.2 2.2 0 0 1 0 4.4z"/></svg>
    <span>Brenmore Timber Co 740 Alder Ridge Rd, Pine Hollow, MN 55012</span>
  </div>
</div>

<header>
  <div class="abs brand"><div class="mark"></div>BRENMORE TIMBER<br>COMPANY</div>
  <nav class="abs nav">
    <a class="active" href="#">HOME</a><a href="#">PRODUCTS</a><a href="#">SERVICES</a><a href="#">COMPANY</a><a href="#">RESOURCES</a><a href="#">CONTACT US</a>
  </nav>
</header>

<section>
  <div class="abs hero" role="img" aria-label="Photo of the lumber yard building with pickup trucks parked on a gravel lot under a cloudy sky"></div>
  <svg class="abs arrow" style="left:62px;top:494px" viewBox="0 0 22 30"><path d="M16 3 4 15l12 12" fill="none" stroke="#fff" stroke-width="3"/></svg>
  <svg class="abs arrow" style="left:1118px;top:494px" viewBox="0 0 22 30"><path d="M6 3l12 12L6 27" fill="none" stroke="#fff" stroke-width="3"/></svg>
  <h1 class="abs hero-title">QUALITY PRODUCTS<br>YOU CAN COUNT ON</h1>
  <a class="abs btn explore" href="#">Explore</a>
  <div class="abs dots"><span class="on"></span><span></span><span></span><span></span><span></span></div>
</section>

<section>
  <h2 class="abs section-title" style="top:838px">QUALITY LUMBER AND CONSTRUCTION PRODUCTS</h2>
  <svg class="abs arrow" style="left:62px;top:1106px" viewBox="0 0 22 30"><path d="M16 3 4 15l12 12" fill="none" stroke="#111" stroke-width="3"/></svg>
  <svg class="abs arrow" style="left:1118px;top:1106px" viewBox="0 0 22 30"><path d="M6 3l12 12L6 27" fill="none" stroke="#111" stroke-width="3"/></svg>

  <h3 class="abs card-title" style="left:144px;top:935px">Lumber</h3>
  <h3 class="abs card-title" style="left:375px;top:935px">Engineered Wood</h3>
  <h3 class="abs card-title" style="left:606px;top:935px">Cabinets</h3>
  <h3 class="abs card-title" style="left:837px;top:935px">Countertops</h3>

  <div class="abs photo" style="left:144px;top:992px;background:linear-gradient(90deg,#a0774c,#b88b5e 40%,#9c7149 70%,#b4895d)" role="img" aria-label="Close-up of weathered wooden planks"></div>
  <div class="abs photo" style="left:375px;top:992px;background:linear-gradient(180deg,#4b5a3e,#6a4a32 50%,#3f4d2c)" role="img" aria-label="Wooden cabin among birch trees in a forest"></div>
  <div class="abs photo" style="left:606px;top:992px;background:linear-gradient(180deg,#d8d6d2,#a9a39b 50%,#4d2c1c)" role="img" aria-label="Modern kitchen with dark cabinets and a pendant light"></div>
  <div class="abs photo" style="left:837px;top:992px;background:linear-gradient(180deg,#eeeeec,#e0ddd8 55%,#5d4a40 70%,#e9e7e4)" role="img" aria-label="White kitchen with a brown stone countertop"></div>

  <p class="abs card-text" style="left:144px;top:1266px">Lorem Ipsum is simply dummy text of the printing and typesetting industry. Lorem Ipsum has been the industry's standard dummy text</p>
  <p class="abs card-text" style="left:375px;top:1266px">Lorem Ipsum is simply dummy text of the printing and typesetting industry. Lorem Ipsum has been the industry's standard dummy text</p>
  <p class="abs card-text" style="left:606px;top:1266px">Lorem Ipsum is simply dummy text of the printing and typesetting industry. Lorem Ipsum has been the industry's standard dummy text</p>
  <p class="abs card-text" style="left:837px;top:1266px">Lorem Ipsum is simply dummy text of the printing and typesetting industry. Lorem Ipsum has been the industry's standard dummy text</p>

  <a class="abs btn small-btn" style="left:167px;top:1374px" href="#">Learn More</a>
  <a class="abs btn small-btn" style="left:399px;top:1374px" href="#">Learn More</a>
  <a class="abs btn small-btn" style="left:628px;top:1374px" href="#">Learn More</a>
  <a class="abs btn small-btn" style="left:860px;top:1374px" href="#">Learn More</a>
</section>

<section>
  <h3 class="abs card-title" style="left:0;width:1200px;top:1476px">Expert Home Improvement Advice</h3>
  <p class="abs lead" style="top:1532px">Lorem Ipsum is simply dummy text of the printing and typesetting industry. Lorem Ipsum has been the industry's standard dummy text ever since the 1500s, when an unknown printer took a galley of type and scrambled it to make a type specimen book</p>
  <a class="abs btn small-btn" style="left:512px;top:1634px" href="#">See More</a>
</section>

<section>
  <h2 class="abs section-title" style="top:1735px">OUR SERVICES</h2>
  <p class="abs lead" style="top:1830px">Lorem Ipsum is simply dummy text of the printing and typesetting industry. Lorem Ipsum has been the industry's standard dummy text ever since the 1500s, when an unknown printer took a galley of type and scrambled it to make a type specimen book. It has survived not only five centuries, but also the leap into electronic typesetting, remaining essentially unchanged. It was popularised in the 1960s with the release of Typeline sheets containing Lorem Ipsum passages, and more recently with desktop publishing software like Quillset Layout including versions of Lorem Ipsum.</p>

  <svg class="abs arrow" style="left:62px;top:2138px" viewBox="0 0 22 30"><path d="M16 3 4 15l12 12" fill="none" stroke="#111" stroke-width="3"/></svg>
  <svg class="abs arrow" style="left:1118px;top:2138px" viewBox="0 0 22 30"><path d="M6 3l12 12L6 27" fill="none" stroke="#111" stroke-width="3"/></svg>

  <h3 class="abs card-title" style="left:144px;top:1967px">House Plans</h3>
  <h3 class="abs card-title" style="left:375px;top:1967px">Cabinet Design</h3>
  <h3 class="abs card-title" style="left:606px;top:1967px">Window Selection</h3>
  <h3 class="abs card-title" style="left:837px;top:1967px">Door Selection</h3>

  <div class="abs photo" style="left:144px;top:2024px;background:linear-gradient(135deg,#5c6b3a,#a9b8c4 45%,#e4e8ea 65%,#6d7a45)" role="img" aria-label="Homeowners reviewing house plans outdoors"></div>
  <div class="abs photo" style="left:375px;top:2024px;background:linear-gradient(180deg,#f1f1ef,#dcdde0 50%,#8e9bb6 80%,#cfcfcd)" role="img" aria-label="Bright kitchen with a blue island and white cabinets"></div>
  <div class="abs photo" style="left:606px;top:2024px;background:linear-gradient(180deg,#a8adb0,#c7cacb 40%,#6d7073 75%,#2f3032)" role="img" aria-label="Dining area with arched windows and grey chairs"></div>
  <div class="abs photo" style="left:837px;top:2024px;background:linear-gradient(90deg,#eef0ea,#7d8b47 20%,#7a4a2a 35%,#8b5a32 65%,#7d8b47 80%,#eef0ea)" role="img" aria-label="Arched wooden front door framed by climbing vines"></div>

  <p class="abs card-text" style="left:144px;top:2298px">Lorem Ipsum is simply dummy text of the printing and typesetting industry. Lorem Ipsum has been the industry's standard dummy text</p>
  <p class="abs card-text" style="left:375px;top:2298px">Lorem Ipsum is simply dummy text of the printing and typesetting industry. Lorem Ipsum has been the industry's standard dummy text</p>
  <p class="abs card-text" style="left:606px;top:2298px">Lorem Ipsum is simply dummy text of the printing and typesetting industry. Lorem Ipsum has been the industry's standard dummy text</p>
  <p class="abs card-text" style="left:837px;top:2298px">Lorem Ipsum is simply dummy text of the printing and typesetting industry. Lorem Ipsum has been the industry's standard dummy text</p>

  <a class="abs btn small-btn" style="left:167px;top:2405px" href="#">Learn More</a>
  <a class="abs btn small-btn" style="left:399px;top:2405px" href="#">Learn More</a>
  <a class="abs btn small-btn" style="left:628px;top:2405px" href="#">Learn More</a>
  <a class="abs btn small-btn" style="left:860px;top:2405px" href="#">Learn More</a>

  <a class="abs btn small-btn quote-btn" style="left:167px;top:2454px" href="#">Get a Quote</a>
  <a class="abs btn small-btn" style="left:399px;top:2454px;box-shadow:0 2px 4px rgba(0,0,0,.35)" href="#">Get a Quote</a>
  <a class="abs btn small-btn quote-btn" style="left:628px;top:2454px" href="#">Get a Quote</a>
  <a class="abs btn small-btn quote-btn" style="left:860px;top:2454px" href="#">Get a Quote</a>

  <a class="abs btn small-btn" style="left:512px;top:2564px" href="#">See More</a>
</section>

<section>
  <div class="abs quote-band" role="img" aria-label="Dimmed photo of the store interior with shelves and service counter"></div>
  <h2 class="abs section-title" style="top:2737px;color:var(--white);letter-spacing:3px">REQUEST A QUOTE</h2>
  <p class="abs lead" style="top:2832px">Lorem Ipsum is simply dummy text of the printing and typesetting industry. Lorem Ipsum has been the industry's standard dummy text ever since the 1500s, when an unknown printer took a galley of type and scrambled it to make a type specimen book. It has survived not only five centuries, but also the leap into electronic typesetting, remaining essentially unchanged. It was popularised in the 1960s with the release of Typeline sheets containing Lorem Ipsum passages, and more recently with desktop publishing software like Quillset Layout including versions of Lorem Ipsum.</p>
  <a class="abs btn small-btn" style="left:512px;top:2978px" href="#">Get a Quote</a>
</section>

<footer>
  <h4 class="abs footer-head" style="left:144px;top:3152px">Site Links</h4>
  <div class="abs links" style="left:144px;top:3240px">HOME<br>PRODUCTS<br>- Product Categories<br>SERVICES<br>- List of services<br>COMPANY<br>- Company Info<br>- Careers<br>- Policies<br>- Testimonials</div>
  <div class="abs links" style="left:339px;top:3240px">RESOURCES<br>- Resource Categories<br>- FAQs<br>- Contractor Directory<br>CONTACT</div>

  <h4 class="abs footer-head" style="left:561px;top:3152px">Company</h4>
  <p class="abs about">Lorem Ipsum is simply dummy text of the printing and typesetting industry. Lorem Ipsum has been the industry's standard dummy text ever since the 1500s, when an unknown printer took a galley of type and scrambled it to make a type specimen book. It has survived not only five centuries, but also the leap into electronic typesetting.</p>
  <div class="abs rule"></div>
  <h4 class="abs footer-head" style="left:561px;top:3398px">Get Social</h4>
  <a class="abs social" style="left:695px;top:3397px;background:#2d64a8" href="#" aria-label="Social profile one"></a>
  <a class="abs social" style="left:748px;top:3397px;background:#2f4f9a" href="#" aria-label="Social profile two"></a>
  <a class="abs social" style="left:801px;top:3397px;background:#c8358a" href="#" aria-label="Social profile three"></a>
  <a class="abs social" style="left:852px;top:3397px;background:#3d9be6" href="#" aria-label="Social profile four"></a>

  <div class="abs bottombar">
    <div class="abs" style="left:144px;top:42px">COPYRIGHT 2018 BRENMORE TIMBER | 740 ALDER RIDGE RD,<br>PINE HOLLOW, MN 55012</div>
    <div class="abs" style="right:144px;top:42px;font-style:italic">PRIVACY POLICY | TERMS OF USE | TERMS AND CONDITIONS OF SALES | DON'T SELL MY INFO</div>
  </div>
</footer>

</body>
</html>
```